Präsentationsvorlagen für die Cloud-Plattform LumaDesk
Zielgruppe
Ich bin ein unabhängiger Berater für die Cloud-Plattform LumaDesk. Zielgruppe sind Unternehmen jeglicher Größe. Das Design sollte schlicht und aufgeräumt sein.
Aufgabenstellung
Dunkler Hintergrund und die Farben aus dem Logo sollten enthalten sein.

```html
<!DOCTYPE html>
<html lang="en">
<head>
<meta charset="utf-8">
<title>LumaDesk Presentation Templates</title>
<link href="https://fonts.googleapis.com/css2?family=Mulish:ital,wght@0,400;0,600;0,700;1,400&display=swap" rel="stylesheet">
<style>
:root{
  --page:#1f1f1f;
  --slide:#141414;
  --orange:#e8822a;
  --blue:#3a8fd0;
  --white:#ffffff;
  --text:#d9d9d9;
  --muted:#8c8c8c;
  --paper:#ffffff;
  --badge:#3a3a3a;
}
*{margin:0;padding:0;box-sizing:border-box}
html,body{width:1200px;height:3599px;overflow:hidden;background:var(--page)}
body{font-family:'Mulish',sans-serif;color:var(--text);position:relative}
.slide{position:absolute;width:514px;height:289px;background:var(--slide);overflow:hidden}
.col-a{left:64px}.col-b{left:622px}
.photo{position:absolute}
.heading{position:absolute;font-size:20px;letter-spacing:2.4px;color:var(--white);font-weight:400;text-transform:uppercase;border-left:1.5px solid var(--orange);padding-left:7px;line-height:1.3}
.heading .accent{color:var(--orange)}
.footer{position:absolute;left:26px;bottom:14px;font-size:5.5px;color:var(--muted)}
.pagenum{position:absolute;right:26px;bottom:13px;font-size:7px;color:var(--orange)}
.brand{position:absolute;right:22px;top:20px;display:flex;align-items:center;gap:3px;font-size:7px;font-weight:700;color:var(--blue)}
.brand i{width:6px;height:6px;border-radius:50%;background:var(--blue);display:block}
.sub{font-size:5.5px;color:var(--orange);font-weight:600;margin-bottom:5px}
.copy{font-size:5.2px;line-height:1.75;color:var(--text)}
.block{position:absolute}
.big-mark{position:absolute;font-weight:700;color:var(--blue)}
.badge{position:absolute;width:36px;height:36px;border-radius:50%;background:var(--badge)}
.cards{position:absolute;left:44px;right:44px;top:82px;display:flex;justify-content:space-between}
.card{width:124px;height:145px;padding:9px 8px;position:relative}
.card-dark{background:#121212}
.card-line{border:1px solid #cfcfcf}
.card-head{display:flex;gap:5px;align-items:center;margin-bottom:10px}
.card-head svg{width:26px;height:26px;flex:none}
.card-title{font-size:5px;font-weight:700;color:var(--white);line-height:1.4}
.card-title span{color:var(--orange)}
.card-title em{display:block;font-style:normal;font-weight:400;color:var(--orange);font-size:4.4px}
.card .copy{font-size:4.5px;line-height:1.7}
.duration{position:absolute;right:8px;bottom:7px;font-size:4.5px;color:var(--text)}
</style>
</head>
<body>

<section class="slide col-a" style="top:319px">
  <div class="photo" role="img" aria-label="Dark monochrome office background photo" style="inset:0;background:linear-gradient(120deg,#191919,#262626 60%,#1b1b1b)"></div>
  <div style="position:absolute;left:46px;top:42px;font-size:19px;letter-spacing:2.4px;font-weight:700;color:var(--orange)">PRESENTATION TITLE</div>
  <div style="position:absolute;left:46px;top:72px;font-size:19px;letter-spacing:2.4px;font-weight:600;color:var(--white)">GOES HERE</div>
  <div class="big-mark" style="right:22px;bottom:40px;font-size:44px">Northbeam</div>
  <div class="footer" style="left:46px">© Northbeam Presentation, 2024</div>
</section>

<section class="slide col-b" style="top:319px">
  <div class="heading" style="left:46px;top:28px">About us</div>
  <div class="brand"><i></i>Northbeam</div>
  <div class="photo" role="img" aria-label="Portrait photo of the consultant in a dark suit" style="left:46px;top:78px;width:208px;height:211px;background:linear-gradient(180deg,#3a3a3a,#1d1d1d)"></div>
  <div class="badge" role="img" aria-label="Certification badge placeholder" style="left:178px;top:196px"></div>
  <div class="block" style="left:256px;top:84px;width:226px">
    <div class="sub">Lorem ipsum dolor sit amet</div>
    <p class="copy">Lorem ipsum dolor sit amet, consectetuer adipiscing elit, sed diam nonummy nibh euismod tincidunt ut laoreet dolore magna aliquam erat volutpat. Ut wisi enim ad minim veniam, quis nostrud exerci tation ullamcorper suscipit lobortis nisl ut aliquip ex ea commodo consequat. Duis autem vel eum iriure dolor in hendrerit in vulputate velit esse mo.</p>
    <p class="copy" style="margin-top:8px">Lorem ipsum dolor sit amet, consectetuer adipiscing elit, sed diam nonummy nibh euismod tincidunt ut laoreet dolore magna aliquam erat volutpat. Ut wisi enim ad minim veniam, quis nostrud exerci tation ullamcorper suscipit lobortis nisl ut aliquip ex ea commodo consequat. Duis autem vel eum iriure dolor in hendrerit in vulputate velit esse mo.</p>
  </div>
  <div class="footer">© Northbeam Presentation, 2024</div>
  <div class="pagenum">| 02</div>
</section>

<section class="slide col-a" style="top:653px">
  <div class="heading" style="left:46px;top:28px"><span class="accent">Page</span> two</div>
  <div class="brand"><i></i>Northbeam</div>
  <div class="block" style="left:46px;top:80px;width:200px">
    <div class="sub">Lorem ipsum dolor sit amet</div>
    <p class="copy">Lorem ipsum dolor sit amet, consectetuer adipiscing elit, sed diam nonummy nibh euismod tincidunt ut laoreet dolore magna aliquam erat volutpat. Ut wisi enim ad minim veniam, quis nostrud exerci tation ullamcorper suscipit lobortis.</p>
    <div class="sub" style="margin-top:14px">Lorem ipsum dolor sit amet</div>
    <p class="copy">Lorem ipsum dolor sit amet, consectetuer adipiscing elit, sed diam nonummy nibh euismod tincidunt ut laoreet dolore magna aliquam erat volutpat. Ut wisi enim ad minim veniam, quis nostrud exerci tation ullamcorper suscipit lobortis.</p>
  </div>
  <div class="block" style="left:278px;top:80px;width:200px">
    <div class="sub">Lorem ipsum dolor sit amet</div>
    <p class="copy">Lorem ipsum dolor sit amet, consectetuer adipiscing elit, sed diam nonummy nibh euismod tincidunt ut laoreet dolore magna aliquam erat volutpat. Ut wisi enim ad minim veniam, quis nostrud exerci tation ullamcorper suscipit lobortis.</p>
    <div class="sub" style="margin-top:14px">Lorem ipsum dolor sit amet</div>
    <p class="copy">Lorem ipsum dolor sit amet, consectetuer adipiscing elit, sed diam nonummy nibh euismod tincidunt ut laoreet dolore magna aliquam erat volutpat. Ut wisi enim ad minim veniam, quis nostrud exerci tation ullamcorper suscipit lobortis.</p>
  </div>
  <div class="footer">© Northbeam Presentation, 2024</div>
  <div class="pagenum">| 03</div>
</section>

<section class="slide col-b" style="top:653px">
  <div class="photo" role="img" aria-label="Photo of a laptop and a coffee cup on a dark desk" style="left:280px;top:0;width:234px;height:289px;background:linear-gradient(160deg,#3b3b3b,#1c1c1c 70%)"></div>
  <div class="heading" style="left:46px;top:60px"><span class="accent">Page</span> three</div>
  <div class="brand"><i></i>Northbeam</div>
  <div class="block" style="left:46px;top:106px;width:200px">
    <p class="copy">Lorem ipsum dolor sit amet, consectetuer adipiscing elit, sed diam nonummy nibh euismod tincidunt ut laoreet dolore magna aliquam erat volutpat. Ut wisi enim ad minim veniam, quis nostrud exerci tation ullamcorper suscipit lobortis.</p>
    <p class="copy" style="margin-top:10px">Lorem ipsum dolor sit amet, consectetuer adipiscing elit, sed diam nonummy nibh euismod tincidunt ut laoreet dolore magna aliquam erat volutpat. Ut wisi enim ad minim veniam, quis nostrud exerci tation ullamcorper suscipit lobortis.</p>
  </div>
  <div class="footer">© Northbeam Presentation, 2024</div>
  <div class="pagenum">| 04</div>
</section>

<section class="slide col-a" style="top:987px">
  <div class="heading" style="left:154px;top:130px"><span class="accent">Our</span> portfolio</div>
</section>

<section class="slide col-b" style="top:987px">
  <div class="photo" role="img" aria-label="Black and white photo of a tall office building" style="left:68px;top:0;width:198px;height:289px;background:linear-gradient(200deg,#6a6a6a,#2a2a2a 70%)"></div>
  <div class="heading" style="left:26px;top:98px"><span class="accent">Solution design</span><br>&amp; architecture</div>
  <div class="brand"><i></i>Northbeam</div>
  <p class="copy block" style="left:296px;top:132px;width:180px">Do you feel the need of overarching technical guidance for your LumaDesk platform? Or do you struggle to find experienced solution architects for your projects? Let me help you by providing independent architecture advisory for projects delivered internally or by LumaDesk partners or act as an interims solution architect providing an unbiased support.</p>
  <div class="footer">© Northbeam Presentation, 2024</div>
  <div class="pagenum">| 06</div>
</section>

<section class="slide col-a" style="top:1321px">
  <div class="photo" role="img" aria-label="Black and white photo of a team meeting in an office" style="left:66px;top:0;width:200px;height:289px;background:linear-gradient(160deg,#555,#252525 75%)"></div>
  <div class="heading" style="left:26px;top:98px"><span class="accent">Platform</span><br><span class="accent">strategy</span> and<br>governance</div>
  <div class="brand"><i></i>Northbeam</div>
  <p class="copy block" style="left:296px;top:130px;width:180px">Are you drowning in daily operations and escalations without a chance to focus on strategic topics? I will help you to develop a long-term strategy and establish a governance structure to allow efficient operation of your LumaDesk platform with an established roadmap, measurable value and a clear decision making process.</p>
  <div class="footer">© Northbeam Presentation, 2024</div>
  <div class="pagenum">| 07</div>
</section>

<section class="slide col-b" style="top:1321px">
  <div class="photo" role="img" aria-label="Dark photo of program code on a screen" style="left:68px;top:0;width:198px;height:289px;background:linear-gradient(180deg,#2c2c2c,#101010)"></div>
  <div class="heading" style="left:26px;top:98px"><span class="accent">Common service</span><br><span class="accent">data model</span><br>(CSDM)</div>
  <div class="brand"><i></i>Northbeam</div>
  <p class="copy block" style="left:296px;top:130px;width:180px">Have you ever wondered what the Common Service Data Model (CSDM) is and how you can benefit from it? I will support you in setting up your business service and offering structure to conform with the CSDM. This will allow you to effectively measure service levels, take better advantage of the LumaDesk products as well as transparent reporting and service costing.</p>
  <div class="footer">© Northbeam Presentation, 2024</div>
  <div class="pagenum">| 08</div>
</section>

<section class="slide col-a" style="top:1655px;background:var(--paper)">
  <div class="heading" style="left:154px;top:130px;color:#1a1a1a"><span class="accent">Recent</span> project</div>
</section>

<section class="slide col-b" style="top:1655px">
  <div style="position:absolute;left:0;top:0;width:514px;height:248px;background:var(--paper)"></div>
  <div class="heading" style="left:144px;top:26px;color:#1a1a1a"><span class="accent">Recent</span> project</div>
  <div class="brand"><i></i>Northbeam</div>
  <div class="cards" style="top:78px">
    <div class="card card-dark">
      <div class="card-head"><svg viewBox="0 0 26 26"><circle cx="13" cy="13" r="10" fill="none" stroke="#e8822a" stroke-width="1.3"/><ellipse cx="13" cy="13" rx="4.5" ry="10" fill="none" stroke="#e8822a" stroke-width="1.1"/><line x1="3" y1="13" x2="23" y2="13" stroke="#e8822a" stroke-width="1.1"/></svg><div class="card-title"><span>CSM &amp; CSDM</span><br>IMPLEMENTATION<em>Industry: Healthcare</em></div></div>
      <p class="copy">Responsibilities: LumaDesk lead architect to develop a target model for the end-to-end customer service processes in Arvano and LumaDesk together with the customer's enterprise architects and Arvano architects.</p>
      <div class="duration">Duration: 5 Months</div>
    </div>
    <div class="card card-dark">
      <div class="card-head"><svg viewBox="0 0 26 26"><rect x="4" y="6" width="10" height="17" fill="none" stroke="#e8822a" stroke-width="1.3"/><rect x="14" y="11" width="8" height="12" fill="none" stroke="#e8822a" stroke-width="1.3"/><path d="M7 10h4M7 14h4M7 18h4M17 15h2M17 19h2" stroke="#e8822a"/></svg><div class="card-title"><span>BUILD CENTER OF</span><br>EXCELLENCE<em>Industry: Automotive</em></div></div>
      <p class="copy">Responsibilities: Support in building up the Center of Excellence and introducing a Demand Management process during the split of two global companies. Overall architectural advisory for platform projects in a multi-vendor environment.</p>
      <div class="duration">Duration: 12 Months</div>
    </div>
    <div class="card card-dark">
      <div class="card-head"><svg viewBox="0 0 26 26"><rect x="5" y="6" width="16" height="11" rx="1" fill="none" stroke="#e8822a" stroke-width="1.3"/><path d="M2 20h22" stroke="#e8822a" stroke-width="1.5"/></svg><div class="card-title"><span>CSDM</span><br>IMPLEMENTATION<em>Industry: Healthcare</em></div></div>
      <p class="copy">Responsibilities: Lead Architect for the initial CSM implementation, define business services, service offerings and application services in accordance to the Common Service Data Model (CSDM), guidance for the platform roadmap planning.</p>
      <div class="duration">Duration: 12 Months</div>
    </div>
  </div>
  <div class="footer">© Northbeam Presentation, 2024</div>
  <div class="pagenum">| 10</div>
</section>

<section class="slide col-a" style="top:1989px">
  <div class="heading" style="left:144px;top:26px"><span class="accent">Recent</span> project</div>
  <div class="brand"><i></i>Northbeam</div>
  <div class="cards" style="top:78px">
    <div class="card card-line">
      <div class="card-head"><svg viewBox="0 0 26 26"><circle cx="13" cy="13" r="10" fill="none" stroke="#e8822a" stroke-width="1.3"/><ellipse cx="13" cy="13" rx="4.5" ry="10" fill="none" stroke="#e8822a" stroke-width="1.1"/><line x1="3" y1="13" x2="23" y2="13" stroke="#e8822a" stroke-width="1.1"/></svg><div class="card-title"><span>CSM &amp; CSDM</span><br>IMPLEMENTATION<em>Industry: Healthcare</em></div></div>
      <p class="copy">Responsibilities: LumaDesk lead architect to develop a target model for the end-to-end customer service processes in Arvano and LumaDesk together with the customer's enterprise architects and Arvano architects.</p>
      <div class="duration">Duration: 5 Months</div>
    </div>
    <div class="card card-line">
      <div class="card-head"><svg viewBox="0 0 26 26"><rect x="4" y="6" width="10" height="17" fill="none" stroke="#e8822a" stroke-width="1.3"/><rect x="14" y="11" width="8" height="12" fill="none" stroke="#e8822a" stroke-width="1.3"/><path d="M7 10h4M7 14h4M7 18h4M17 15h2M17 19h2" stroke="#e8822a"/></svg><div class="card-title"><span>BUILD CENTER OF</span><br>EXCELLENCE<em>Industry: Automotive</em></div></div>
      <p class="copy">Responsibilities: Support in building up the Center of Excellence and introducing a Demand Management process during the split of two global companies. Overall architectural advisory for platform projects in a multi-vendor environment.</p>
      <div class="duration">Duration: 12 Months</div>
    </div>
    <div class="card card-line">
      <div class="card-head"><svg viewBox="0 0 26 26"><rect x="5" y="6" width="16" height="11" rx="1" fill="none" stroke="#e8822a" stroke-width="1.3"/><path d="M2 20h22" stroke="#e8822a" stroke-width="1.5"/></svg><div class="card-title"><span>CSDM</span><br>IMPLEMENTATION<em>Industry: Healthcare</em></div></div>
      <p class="copy">Responsibilities: Lead Architect for the initial CSM implementation, define business services, service offerings and application services in accordance to the Common Service Data Model (CSDM), guidance for the platform roadmap planning.</p>
      <div class="duration">Duration: 12 Months</div>
    </div>
  </div>
  <div style="position:absolute;left:0;bottom:0;width:514px;height:38px;background:var(--orange)"></div>
  <div class="footer" style="color:var(--white)">© Northbeam Presentation, 2024</div>
  <div class="pagenum" style="color:var(--white)">| 11</div>
</section>

<section class="slide col-b" style="top:1989px">
  <div class="heading" style="left:46px;top:28px"><span class="accent">Quote</span></div>
  <div class="brand"><i></i>Northbeam</div>
  <div style="position:absolute;left:36px;top:56px;font-size:70px;font-weight:700;color:var(--orange);opacity:.55;line-height:1">“</div>
  <p style="position:absolute;left:54px;top:92px;width:420px;font-size:14px;font-style:italic;color:var(--white);line-height:1.5">We cannot solve problems with the kind of thinking we employed when we came up with them.</p>
  <div style="position:absolute;right:50px;top:144px;font-size:8.5px;font-style:italic;color:var(--white)">— Hugo Brenner</div>
  <p class="copy block" style="left:54px;top:170px;width:420px">Lorem ipsum dolor sit amet, consectetuer adipiscing elit, sed diam nonummy nibh euismod tincidunt ut laoreet dolore magna aliquam erat volutpat. Ut wisi enim ad minim veniam, quis nostrud exerci tation ullamcorper suscipit lobortis nisl ut aliquip ex ea commodo consequat. Duis autem vel eum iriure dolor in hendrerit in vulputate velit esse mo.</p>
  <div class="footer">© Northbeam Presentation, 2024</div>
  <div class="pagenum">| 12</div>
</section>

<section class="slide col-a" style="top:2323px">
  <div class="photo" role="img" aria-label="Black and white photo of a modern building facade with orange tint below" style="left:38px;top:0;width:196px;height:228px;background:linear-gradient(180deg,#5a5a5a 0%,#2e2e2e 62%,#c0702a 63%,#e8822a 100%)"></div>
  <div class="heading" style="left:280px;top:28px"><span class="accent">Page</span> four</div>
  <div class="brand"><i></i>Northbeam</div>
  <div class="block" style="left:280px;top:80px;width:200px">
    <div class="sub">Lorem ipsum dolor sit amet</div>
    <p class="copy">Lorem ipsum dolor sit amet, consectetuer adipiscing elit, sed diam nonummy nibh euismod tincidunt ut laoreet dolore magna aliquam erat volutpat. Ut wisi enim ad minim veniam, quis nostrud exerci tation ullamcorper suscipit lobortis.</p>
    <div class="sub" style="margin-top:12px">Lorem ipsum dolor sit amet</div>
    <p class="copy">Lorem ipsum dolor sit amet, consectetuer adipiscing elit, sed diam nonummy nibh euismod tincidunt ut laoreet dolore magna aliquam erat volutpat. Ut wisi enim ad minim veniam, quis nostrud exerci tation ullamcorper suscipit lobortis.</p>
  </div>
  <div class="footer">© Northbeam Presentation, 2024</div>
  <div class="pagenum">| 13</div>
</section>

<section class="slide col-b" style="top:2323px">
  <div class="photo" role="img" aria-label="Black and white photo of a person working on a laptop" style="left:0;top:0;width:514px;height:142px;background:linear-gradient(90deg,#262626,#4a4a4a 55%,#2a2a2a)"></div>
  <div class="brand"><i></i>Northbeam</div>
  <div class="heading" style="left:34px;top:176px"><span class="accent">Page</span> five</div>
  <div class="block" style="left:212px;top:168px;width:270px">
    <div class="sub">Lorem ipsum dolor sit amet</div>
    <p class="copy">Lorem ipsum dolor sit amet, consectetuer adipiscing elit, sed diam nonummy nibh euismod tincidunt ut laoreet dolore magna aliquam erat volutpat. Ut wisi enim ad minim veniam, quis nostrud exerci tation ullamcorper suscipit lobortis. Lorem ipsum dolor sit amet, consectetuer adipiscing elit, sed diam nonummy nibh euismod tincidunt ut laoreet dolore magna aliquam erat volutpat. Ut wisi enim ad minim veniam, quis nostrud exerci.</p>
  </div>
  <div class="footer">© Northbeam Presentation, 2024</div>
  <div class="pagenum">| 14</div>
</section>

<section class="slide col-a" style="top:2657px">
  <div class="heading" style="left:46px;top:28px"><span class="accent">Page</span> six</div>
  <div class="brand"><i></i>Northbeam</div>
  <p class="copy block" style="left:46px;top:76px;width:420px">Lorem ipsum dolor sit amet, consectetuer adipiscing elit, sed diam nonummy nibh euismod tincidunt ut laoreet dolore magna aliquam erat volutpat. Ut wisi enim ad minim veniam, quis nostrud exerci tation ullamcorper suscipit lobortis nisl ut aliquip ex ea commodo consequat. Duis autem vel eum iriure dolor in hendrerit in vulputate velit esse molestie consequat, vel illum dolore eu feugiat nulla facilisis at vero eros et accumsan et iusto odio dignissim qui blandit praesent luptatum zzril delenit augue duis dolore te feugait nulla facilisi. Lorem ipsum dolor sit amet, cons ectetuer adipiscing elit, sed diam nonummy nibh euismod tincidunt ut laoreet dolore magna aliquam erat volutpat. Ut wisi enim ad minim veniam, quis nostrud exerci tation ullamcorper suscipit lobortis nisl ut aliquip ex ea commodo consequat. Lorem ipsum dolor sit amet, consectetuer adipiscing elit, sed diam nonummy nibh euismod tincidunt ut laoreet dolore magna aliquam erat volutpat. Ut wisi enim ad minim veniam, quis nostrud exerci tation ullamcorper suscipit lobortis nisl ut aliquip ex ea commodo consequat. Duis autem vel eum iriure dolor in hendrerit in vulputate velit esse molestie consequat, vel illum dolore eu feugiat nulla facilisis at vero eros et accumsan. Lorem ipsum dolor sit amet, cons ectetuer adipiscing elit, sed diam nonummy nibh euismod tincidunt ut laoreet dolore magna aliquam erat volutpat.</p>
  <div class="footer">© Northbeam Presentation, 2024</div>
  <div class="pagenum">| 15</div>
</section>

<section class="slide col-b" style="top:2657px">
  <div class="photo" role="img" aria-label="Faint dark background photo" style="inset:0;background:linear-gradient(135deg,#161616,#202020)"></div>
  <div class="heading" style="left:154px;top:28px"><span class="accent">Any</span> question?</div>
  <div class="block" style="left:46px;top:88px;width:160px;font-size:7.5px;color:var(--text);line-height:1.6">
    <div>Ahornweg 12, 55270<br>Kleinhofen, Germany</div>
    <div style="border-top:1px solid var(--orange);margin:10px 0 8px"></div>
    <div>(+49) 170 555 01 234</div>
    <div style="border-top:1px solid var(--orange);margin:10px 0 8px"></div>
    <div>lena@northbeam-consult.com</div>
    <div style="border-top:1px solid var(--orange);margin:10px 0 8px"></div>
    <div>www.northbeam-consult.com</div>
  </div>
  <div class="big-mark" style="right:22px;bottom:40px;font-size:44px">Northbeam</div>
</section>

</body>
</html>
```